Business Cards for accounting firm

Need a file and design that we can update for our employees when we get a design we like. Logo is attached.
Megan Tolliver CPA
Owner
P.O. Box 418
Perrysburg OH 43187
4193628405
megan@brightlanefin.com
www.brightlanefin.com
Accounting

```html
<!DOCTYPE html>
<html lang="en">
<head>
<meta charset="utf-8">
<title>Brightlane Financial – Business Card</title>
<link rel="stylesheet" href="https://fonts.googleapis.com/css2?family=Lato:wght@400;700;900&display=swap">
<style>
  :root {
    --page-bg: #ecebe8;
    --card-grey: #6a6b6e;
    --card-grey-light: #7a7b7e;
    --card-grey-dark: #5c5d60;
    --brand-blue: #22a6e0;
    --ink-grey: #5e5f62;
    --paper: #ffffff;
    --paper-shade: #f1f1f1;
    --logo-light: #ececec;
  }
  * { box-sizing: border-box; margin: 0; padding: 0; }
  html, body {
    width: 1200px; height: 900px; overflow: hidden;
    background: var(--page-bg);
    font-family: "Lato", Arial, sans-serif;
  }
  .sheet {
    width: 1200px; height: 900px;
    display: flex; align-items: center; justify-content: center; gap: 40px;
  }
  .card {
    width: 540px; height: 309px; position: relative; overflow: hidden;
    box-shadow: 0 6px 18px rgba(0,0,0,.18);
  }

  /* Back */
  .card-back {
    background: radial-gradient(ellipse at 40% 40%, var(--card-grey-light), var(--card-grey) 55%, var(--card-grey-dark));
    display: flex; align-items: center; justify-content: center;
  }
  .wordmark {
    font-weight: 900; letter-spacing: -0.5px; line-height: 1; text-align: center;
  }
  .card-back .wordmark { color: var(--logo-light); font-size: 50px; }

  /* Front */
  .card-front { background: var(--paper); }
  .front-top {
    position: absolute; left: 0; top: 0; width: 100%; height: 140px;
    background: linear-gradient(180deg, var(--paper), var(--paper-shade));
    display: flex; align-items: center; justify-content: center;
  }
  .card-front .wordmark { color: var(--ink-grey); font-size: 42px; }
  .contact-band {
    position: absolute; left: 0; top: 140px; width: 100%; height: 132px;
    background: var(--brand-blue); color: var(--paper);
    display: flex; align-items: center; justify-content: space-between;
    padding: 0 40px 0 30px;
  }
  .base-strip {
    position: absolute; left: 0; bottom: 0; width: 100%; height: 37px;
    background: var(--card-grey);
  }
  .person { text-align: center; width: 250px; }
  .person-name { font-size: 21px; font-weight: 700; }
  .person-title { font-size: 14px; margin-top: 1px; }
  .person-address { font-size: 16px; margin-top: 10px; line-height: 1.25; }
  .contact-list { list-style: none; font-size: 14px; }
  .contact-list li { display: flex; align-items: center; gap: 7px; height: 22px; }
  .contact-icon { width: 14px; height: 14px; flex: none; }
</style>
</head>
<body>
<main class="sheet">
  <section class="card card-back" aria-label="Card back">
    <div class="wordmark">Brightlane<br>Financial</div>
  </section>

  <section class="card card-front" aria-label="Card front">
    <header class="front-top">
      <div class="wordmark">Brightlane<br>Financial</div>
    </header>
    <div class="contact-band">
      <div class="person">
        <p class="person-name">John Smith</p>
        <p class="person-title">Managing Director</p>
        <p class="person-address">1234, Address GoesHere<br>Country, 12345</p>
      </div>
      <ul class="contact-list">
        <li>
          <svg class="contact-icon" viewBox="0 0 14 14" aria-hidden="true"><rect width="14" height="14" rx="2" fill="#fff"/><path d="M4 3.5c-.6.4-.8 1.2-.5 2 .8 2 2.5 3.7 4.5 4.5.8.3 1.6.1 2-.5l-1.5-1.3-1 .6c-1-.5-1.8-1.3-2.3-2.3l.6-1z" fill="#22a6e0"/></svg>
          123-456-7890
        </li>
        <li>
          <svg class="contact-icon" viewBox="0 0 14 14" aria-hidden="true"><rect width="14" height="14" rx="2" fill="#fff"/><rect x="3" y="5.5" width="8" height="5" fill="#22a6e0"/><rect x="4.5" y="3" width="5" height="3" fill="none" stroke="#22a6e0"/></svg>
          123-456-7890
        </li>
        <li>
          <svg class="contact-icon" viewBox="0 0 14 14" aria-hidden="true"><rect width="14" height="14" rx="2" fill="#fff"/><rect x="3" y="4" width="8" height="6" fill="#22a6e0"/><path d="M3 4l4 3.2L11 4" fill="none" stroke="#fff" stroke-width="1"/></svg>
          info@youremail.com
        </li>
        <li>
          <svg class="contact-icon" viewBox="0 0 14 14" aria-hidden="true"><rect width="14" height="14" rx="2" fill="#fff"/><path d="M6 8l2-2M5.2 6.8l-1 1a1.4 1.4 0 002 2l1-1M8.8 7.2l1-1a1.4 1.4 0 00-2-2l-1 1" fill="none" stroke="#22a6e0" stroke-width="1.2" stroke-linecap="round"/></svg>
          www.yourweb.com
        </li>
      </ul>
    </div>
    <div class="base-strip"></div>
  </section>
</main>
</body>
</html>
```